house selling company website

i need a website that is to get customers to let us sell their house within 30 days with no sales fees based in the uk. iv uploaded a design i like for the website i own i want a copy of this but for the different logo ect need the house buying logo i own to be changed to house selling company
it needs to be able to flash up to sell your house today contact box to collect their details such as property type, address, number of bedrooms, (estate agents valuation) , best price you can accept after they have seen the main section banner with advertising why use us.
the three reasons in the banner to use us needs to be
1: We will sell your house in 30 days and ensure we take a buyers fee for our service from the buyer meaning your buyer is secured unlike with most estate agents
2: We do not charge you any fees at all! our small fee is charged to the buyer
3: A huge network of investors and private buyers connecting many estate agents, auction houses, investors, and private buyers to ensure a fast sale.

```html
<!DOCTYPE html>
<html lang="en">
<head>
<meta charset="utf-8">
<title>HomeswiftSales – Sell your home fast</title>
<link rel="stylesheet" href="https://fonts.googleapis.com/css2?family=Roboto:wght@400;500;700&display=swap">
<style>
:root{
  --sky:#b9eefc;
  --brand:#1b95d1;
  --brand-dark:#1488c4;
  --white:#ffffff;
  --number:#3aa6dc;
  --ring:#c3f1fd;
}
*{margin:0;padding:0;box-sizing:border-box}
html,body{width:869px;height:1200px;overflow:hidden}
body{position:relative;background:var(--sky);font-family:"Roboto",sans-serif;color:var(--brand)}
.abs{position:absolute}
.brand-name{font-size:10.5px;font-weight:500;color:var(--brand);letter-spacing:.1px}
.nav a{position:absolute;top:38px;font-size:8.5px;color:var(--brand);text-decoration:none}
.btn{position:absolute;top:32px;height:25px;border-radius:3px;font-size:9px;font-weight:700;display:flex;align-items:center;justify-content:center}
.btn-login{left:656px;width:58px;background:var(--brand);color:var(--white)}
.btn-register{left:721px;width:59px;border:1px solid var(--brand);color:var(--brand)}
.hero-title{top:110px;left:0;width:869px;text-align:center;font-size:33px;line-height:38px;font-weight:700;color:var(--brand)}
.hero-scene{top:178px;left:0;width:869px;height:323px;background:linear-gradient(180deg,#b9eefc 0%,#d9d3ea 30%,#a98bbf 58%,#6a7fb0 76%,#4d85b8 82%,#6f9fcc 100%)}
.search-panel{top:408px;left:147px;width:575px;height:80px;background:var(--brand);border-radius:5px}
.field-label{position:absolute;top:16px;font-size:8px;font-weight:700;color:var(--white)}
.field{position:absolute;top:30px;width:145px;height:29px;border:1px solid var(--white);border-radius:3px;color:var(--white);font-size:8px;font-weight:500;display:flex;align-items:center;padding-left:5px}
.field svg{position:absolute;right:9px;top:12px}
.search-btn{position:absolute;top:30px;left:473px;width:86px;height:29px;background:var(--white);border-radius:3px;color:var(--brand);font-size:11px;display:flex;align-items:center;justify-content:center}
.section-title{top:530px;left:0;width:869px;text-align:center;font-size:27px;font-weight:700;color:var(--brand)}
.card{position:absolute;top:600px;width:214px;height:285px;background:var(--brand);border-radius:4px}
.card-number{position:absolute;left:2px;top:0;font-size:40px;font-weight:700;color:var(--number);line-height:48px}
.card-art{position:absolute;left:37px;top:20px;width:140px;height:140px;border-radius:50%;border:5px solid var(--ring)}
.card-text{position:absolute;left:10px;top:181px;width:194px;text-align:center;font-size:11px;line-height:13.7px;font-weight:500;color:var(--white)}
.skyline{top:935px;left:0;width:869px;height:125px;background:linear-gradient(180deg,var(--sky) 0%,#6cc3ea 45%,var(--brand) 100%)}
.footer{top:1060px;left:0;width:869px;height:140px;background:var(--brand)}
.footer-col{position:absolute;color:var(--white)}
.footer h3{font-size:13px;font-weight:500;margin-bottom:3px}
.footer p,.footer li{font-size:8px;line-height:13.6px;list-style:none}
.follow li{display:flex;align-items:center;gap:3px;line-height:18.3px}
.dot{width:13px;height:13px;border-radius:50%;background:var(--white);display:inline-block}
.input{width:178px;height:23px;background:var(--white);border-radius:3px;font-size:8px;color:var(--brand);padding:7px 12px;margin-bottom:6px}
.subscribe{width:67px;height:24px;background:var(--white);border-radius:3px;font-size:11px;color:var(--brand);display:flex;align-items:center;justify-content:center}
.copyright{top:1157px;left:88px;font-size:8px;color:var(--white)}
</style>
</head>
<body>
<header>
  <div class="abs" style="left:89px;top:36px"><span class="brand-name">HomeswiftSales</span></div>
  <nav class="nav">
    <a style="left:345px" href="#">Home</a>
    <a style="left:403px" href="#">About us</a>
    <a style="left:472px" href="#">Buy my house</a>
  </nav>
  <div class="btn btn-login">Login</div>
  <div class="btn btn-register">Register</div>
</header>

<h1 class="abs hero-title">THE FASTEST WAY TO BUY<br>YOUR SOCIAL HOME</h1>
<div class="abs hero-scene" role="img" aria-label="Illustrated city skyline at sunrise reflected in water"></div>

<form class="abs search-panel">
  <span class="field-label" style="left:19px">Location</span>
  <span class="field-label" style="left:170px">Bedrooms</span>
  <span class="field-label" style="left:320px">Max. Rent ($ Per month )</span>
  <div class="field" style="left:17px">Twown or post code<svg width="7" height="4"><path d="M0 0h7L3.5 4z" fill="#fff"/></svg></div>
  <div class="field" style="left:169px">Any</div>
  <div class="field" style="left:320px">Any<svg width="7" height="4"><path d="M0 0h7L3.5 4z" fill="#fff"/></svg></div>
  <div class="search-btn">Search</div>
</form>

<h2 class="abs section-title">WHY CHOOSE US</h2>

<section class="reasons">
  <article class="card" style="left:94px">
    <span class="card-number">01</span>
    <div class="card-art" style="background:#dcecf8" role="img" aria-label="Icon of an address book"></div>
    <p class="card-text">We will sell your house in 30 days and ensure we take a buyers fee for our service from the buyer meaning your buyer is secured unlike with most estate agents</p>
  </article>
  <article class="card" style="left:325px">
    <span class="card-number">02</span>
    <div class="card-art" style="background:#e9eef4" role="img" aria-label="Illustration of two people meeting at a laptop"></div>
    <p class="card-text">We do not charge you any fees at all! our small fee is charged to the buyer</p>
  </article>
  <article class="card" style="left:555px">
    <span class="card-number">03</span>
    <div class="card-art" style="background:#e2e6ea" role="img" aria-label="Icon of office buildings"></div>
    <p class="card-text">A huge network of investors and private buyers connecting many estate agents, auction houses, investors, and private buyers to ensure a fast sale.</p>
  </article>
</section>

<div class="abs skyline" role="img" aria-label="City skyline silhouette"></div>

<footer class="abs footer">
  <div class="footer-col" style="left:89px;top:-27px"><span class="brand-name" style="color:#fff">HomeswiftSales</span></div>
  <div class="footer-col" style="left:89px;top:18px;width:160px">
    <p>Lorem Ipsum is simply dummy text of the printing and typesetting industry. Lorem Ipsum has been the industry's standard dummy text ever since the 1500s, when</p>
  </div>
  <div class="footer-col" style="left:300px;top:1px">
    <h3>Menu</h3>
    <ul><li>Home</li><li>About Us</li><li>Buy my house</li></ul>
  </div>
  <div class="footer-col follow" style="left:413px;top:1px">
    <h3>Follow Us</h3>
    <ul><li><span class="dot"></span>Picstream</li><li><span class="dot"></span>Chatterly</li><li><span class="dot"></span>Linkspace</li><li><span class="dot"></span>Clipcast</li></ul>
  </div>
  <div class="footer-col" style="left:545px;top:1px">
    <h3>Newsletter</h3>
    <div class="input">Name</div>
    <div class="input">Address</div>
    <div class="subscribe">Subscribe</div>
  </div>
</footer>
<p class="abs copyright">Copyright © 2010-2023 homeswift sales. All rights reserved.</p>
</body>
</html>
```